Become an EMT and Serve your community!

We are looking to design a postcard that will be mailed to surrounding communities that notifies them of our upcoming EMT class with an emphasis of serving their community. We are looking for a design that grabs peoples attention and motivates them to sign up and serve their community. Our primary colors are red and blue. We would like to incorporate the Institute logo as well as one or two photos. We do have more photos available upon request. Our Institute website is www.halvorsenacademy.net for more material. It is important that the postcard meets mailing guidelines.

Target Market(s)

Local community members

Industry/Entity Type

Education

Font styles to use
Sans Serif

Colors
f04a50
3176b5
0255a3
eaf1f7

Requirements
Must have
• Dates
Prices
Contact info
Look interesting
Convey the message of “Serving your Community”
Nice to have
• Clear information
Concise
Incorporate an action shot
Should not have
• Generic EMS logos

```html
<!DOCTYPE html>
<html lang="en">
<head>
<meta charset="utf-8">
<title>2020 Summer EMT Class – Postcard</title>
<link rel="stylesheet" href="https://fonts.googleapis.com/css2?family=Roboto+Condensed:wght@700&family=Roboto:wght@400;700&display=swap">
<style>
  :root {
    --red: #c8102e;
    --red-deep: #b0121e;
    --blue: #2a5ba8;
    --blue-dark: #1f4e9c;
    --blue-light: #eaf1f7;
    --sky: #cfe3f6;
    --ink: #1a1a1a;
    --white: #ffffff;
    --page: #efefef;
  }
  * { box-sizing: border-box; margin: 0; padding: 0; }
  html, body { width: 1200px; height: 1000px; overflow: hidden; }
  body {
    position: relative;
    background: var(--page);
    font-family: "Roboto", Arial, sans-serif;
    color: var(--ink);
  }

  /* ---------- Front ---------- */
  .card-front {
    position: absolute; left: 248px; top: 17px; width: 717px; height: 463px;
    background: linear-gradient(120deg, #f4f9fe 0%, var(--blue-light) 35%, var(--sky) 70%);
    overflow: hidden;
  }
  .corner-flag { position: absolute; left: 0; top: 0; }
  .front-photo {
    position: absolute; left: 0; top: 0; width: 717px; height: 391px;
    background: linear-gradient(135deg, #d8d8d8 0%, #8f8f8f 40%, #b83a33 60%, #5a5a5a 100%);
    clip-path: polygon(268px 391px, 520px 0, 717px 0, 717px 391px);
  }
  .front-stripes { position: absolute; left: 0; top: 0; }
  .front-title {
    position: absolute; left: 24px; top: 36px;
    font-family: "Roboto Condensed", "Arial Narrow", sans-serif;
    font-weight: 700; font-size: 58px; line-height: 58px;
    color: var(--red);
  }
  .front-tagline {
    position: absolute; left: 24px; top: 169px; width: 270px;
    border-left: 4px solid var(--red);
    padding-left: 9px;
    font-size: 20px; line-height: 25px; color: var(--ink);
  }
  .front-brands {
    position: absolute; left: 24px; top: 285px;
    display: flex; gap: 10px;
  }
  .brand {
    display: flex; align-items: center; gap: 6px;
    font-family: "Roboto", Arial, sans-serif; font-weight: 700;
    font-size: 12px; line-height: 14px;
  }
  .brand-dot { width: 14px; height: 14px; border-radius: 50%; flex: none; }
  .brand--blue { color: var(--blue-dark); }
  .brand--blue .brand-dot { background: var(--blue-dark); }
  .brand--red { color: var(--red-deep); }
  .brand--red .brand-dot { background: var(--red-deep); }
  .front-footer {
    position: absolute; left: 0; top: 391px; width: 717px; height: 72px;
    background: var(--blue); color: var(--white);
    padding: 12px 0 0 22px;
  }
  .front-footer .dates {
    font-family: "Roboto Condensed", "Arial Narrow", sans-serif;
    font-weight: 700; font-size: 24px; line-height: 28px;
  }
  .front-footer .labs { font-size: 13px; line-height: 18px; }

  /* ---------- Back ---------- */
  .card-back {
    position: absolute; left: 248px; top: 507px; width: 717px; height: 463px;
    background: var(--white); overflow: hidden;
  }
  .back-register {
    position: absolute; left: 25px; top: 22px; width: 200px;
  }
  .back-register h2 {
    font-family: "Roboto Condensed", "Arial Narrow", sans-serif;
    font-weight: 700; font-size: 21px; line-height: 26px; color: var(--red);
  }
  .web-pill {
    display: inline-block; margin-top: 8px;
    background: var(--red-deep); color: var(--white);
    font-size: 11px; line-height: 20px; padding: 0 9px; border-radius: 10px;
  }
  .tuition { margin-top: 9px; font-size: 10px; line-height: 12px; }
  .back-photo {
    position: absolute; left: 207px; top: 0; width: 307px; height: 158px;
    background: linear-gradient(160deg, #6e6a64 0%, #3b6fa8 45%, #c9b79a 75%, #4a4e5c 100%);
  }
  .features {
    position: absolute; left: 0; top: 158px; width: 514px; height: 170px;
    background: var(--blue); display: flex;
  }
  .feature {
    flex: 1; display: flex; flex-direction: column; align-items: center;
    padding-top: 38px; color: var(--white);
    font-size: 12.5px; line-height: 15px; text-align: center;
    border-right: 1px solid rgba(0,0,0,0.18);
  }
  .feature:last-child { border-right: none; }
  .feature svg { margin-bottom: 16px; }
  .schedule {
    position: absolute; left: 0; top: 328px; width: 514px; height: 105px;
    background: linear-gradient(90deg, var(--sky) 0%, #f3f8fd 30%, #f3f8fd 70%, var(--sky) 100%);
    text-align: center; font-size: 12px; line-height: 15px; padding: 9px 14px 0;
  }
  .schedule strong { font-weight: 700; }
  .schedule p + p { margin-top: 14px; }
  .back-footer {
    position: absolute; left: 0; top: 433px; width: 514px; height: 30px;
    background: var(--blue);
  }
  .postage {
    position: absolute; left: 635px; top: 21px; width: 63px; height: 63px;
    border: 1px solid var(--ink);
    font-size: 9px; line-height: 11px; text-align: center; padding-top: 15px;
  }
  .address-line {
    position: absolute; left: 534px; width: 162px; height: 1px; background: var(--ink);
  }
  .back-brands {
    position: absolute; left: 548px; top: 382px;
    display: flex; flex-direction: column; gap: 10px;
  }
</style>
</head>
<body>

  <section class="card-front">
    <div class="front-photo" role="img" aria-label="Photo of two EMTs in red jackets treating a patient inside an ambulance"></div>
    <svg class="front-stripes" width="717" height="391" viewBox="0 0 717 391" aria-hidden="true">
      <polygon points="232,391 256,391 508,0 484,0" fill="#2a5ba8" opacity="0.85"/>
      <polygon points="262,391 268,391 520,0 514,0" fill="#1f4e9c"/>
      <polygon points="585,55 600,55 620,25 605,25" fill="#1f4e9c"/>
    </svg>
    <svg class="corner-flag" width="40" height="32" viewBox="0 0 40 32" aria-hidden="true">
      <polygon points="0,0 40,0 0,32" fill="#2a5ba8"/>
    </svg>

    <h1 class="front-title">2020 Summer<br>EMT Class</h1>
    <p class="front-tagline">Serve your community and become an Emergency Medical Technician!</p>

    <div class="front-brands">
      <div class="brand brand--blue"><span class="brand-dot"></span>Halvorsen<br>Institute</div>
      <div class="brand brand--red">Halvorsen<br>Memorial EMS</div>
    </div>

    <div class="front-footer">
      <div class="dates">Monday, Tuesday, Wednesday from May 26th through August 17th</div>
      <div class="labs">Wednesdays: Students will need to sign up for either a 4:00PM-7:00PM lab section, or a 7:00PM-10:PM lab section</div>
    </div>
  </section>

  <section class="card-back">
    <svg class="corner-flag" width="40" height="32" viewBox="0 0 40 32" aria-hidden="true">
      <polygon points="0,0 40,0 0,32" fill="#2a5ba8"/>
    </svg>
    <div class="back-register">
      <h2>Register for an<br>EMT CLASS NOW!</h2>
      <span class="web-pill">www.halvorsenacademy.net</span>
      <p class="tuition"><strong>TUITION:</strong> $1000 EMT (without CPR)<br>$250 deposit due at time of registration</p>
    </div>
    <div class="back-photo" role="img" aria-label="Action photo of students practising airway care on a training manikin"></div>

    <div class="features">
      <div class="feature">
        <svg width="48" height="42" viewBox="0 0 48 42" fill="none" stroke="#fff" stroke-width="2" aria-hidden="true">
          <rect x="3" y="2" width="42" height="30" rx="2"/>
          <rect x="8" y="7" width="32" height="20"/>
          <polyline points="10,18 17,18 20,11 24,24 27,15 30,18 38,18"/>
          <line x1="24" y1="32" x2="24" y2="38"/><line x1="14" y1="39" x2="34" y2="39"/>
        </svg>
        Access to cutting edge<br>training equipment
      </div>
      <div class="feature">
        <svg width="40" height="44" viewBox="0 0 40 44" fill="none" stroke="#fff" stroke-width="2" aria-hidden="true">
          <path d="M10 12 a10 10 0 0 1 20 0 v4 h-20 z"/>
          <path d="M11 16 v3 a9 9 0 0 0 18 0 v-3"/>
          <path d="M3 43 v-8 a8 8 0 0 1 8 -8 h18 a8 8 0 0 1 8 8 v8 z"/>
          <line x1="20" y1="27" x2="20" y2="43"/>
        </svg>
        Experienced<br>Instructors
      </div>
      <div class="feature">
        <svg width="66" height="42" viewBox="0 0 66 42" fill="none" stroke="#fff" stroke-width="2" aria-hidden="true">
          <path d="M2 8 h40 v26 h-40 z"/>
          <path d="M42 14 h12 l9 10 v10 h-21"/>
          <circle cx="14" cy="35" r="4" fill="#2a5ba8"/><circle cx="52" cy="35" r="4" fill="#2a5ba8"/>
          <path d="M19 15 v12 M13 21 h12"/>
          <path d="M44 3 h6 v5 h-6 z"/>
        </svg>
        Train on a 911<br>Ambulance
      </div>
    </div>

    <div class="schedule">
      <p><strong>Monday, Tuesday, Wednesday from May 26th through August 17th.</strong><br>
      Wednesdays: Students will need to sign up for either a 4:00p-7:00p lab section, or a 7:00p-10:0p lab section.</p>
      <p>There will be one required Sat/Sun weekend held for all students. This will take place on June 13th &amp; 14th. Weekend classes will run from 8:00am - 8:00pm.</p>
    </div>
    <div class="back-footer"></div>

    <div class="postage">US<br>POSTAGE<br>PAID</div>
    <div class="address-line" style="top:166px"></div>
    <div class="address-line" style="top:187px"></div>
    <div class="address-line" style="top:207px"></div>

    <div class="back-brands">
      <div class="brand brand--blue"><span class="brand-dot"></span>Halvorsen Institute</div>
      <div class="brand brand--red">Halvorsen Memorial EMS</div>
    </div>
  </section>

</body>
</html>
```